deceased estate clean ups brochures

we would like a brochure to reresent our business we already have new web site and want to do DL A4 brochure to give out to promote our business we already have logo www.larkmore.com.au is where you can get all info needed

Target Market(s)

families with loved ones that have past away
people done sizing or needing to decluter

Colors
cadf82
33b8a4
886aae
33a6d7

```html
<!DOCTYPE html>
<html lang="en">
<head>
<meta charset="utf-8">
<title>Larkmore – Deceased Estate Cleanups Brochure</title>
<link rel="stylesheet" href="https://fonts.googleapis.com/css2?family=Montserrat:ital,wght@0,400;0,600;0,700;0,800;1,400;1,700;1,800&family=Archivo+Black&display=swap">
<style>
:root{
  --green:#78b843;
  --green-light:#cadf82;
  --green-pale:#e6f1d3;
  --ink:#2b2b2b;
  --text:#4a4a4a;
  --paper:#ffffff;
  --tile:#d8d8d8;
  --tile-dark:#c9c9c9;
  --stage:#e4e4e4;
  --brick:#a65a3e;
}
*{box-sizing:border-box;margin:0;padding:0}
html,body{width:686px;height:1200px;overflow:hidden}
body{background:var(--stage);font-family:'Montserrat',sans-serif;color:var(--text);position:relative}
.spread{position:absolute;left:20px;width:646px;height:500px;background:var(--paper);display:flex;box-shadow:0 6px 18px rgba(0,0,0,.18)}
.spread--outside{top:50px}
.spread--inside{top:620px}
.panel{position:relative;width:215.33px;height:100%;overflow:hidden;border-right:1px solid #eee}
.panel:last-child{border-right:none}
.abs{position:absolute}
.photo{position:absolute;display:block}
.photo--warm{background:linear-gradient(160deg,#c07a5a 0%,#a65a3e 45%,#d9cdbb 100%)}
.photo--couple{background:linear-gradient(160deg,#b86a4d 0%,#a65a3e 35%,#c9c9d6 65%,#5a6f95 100%)}
.photo--clean{background:linear-gradient(135deg,#f2f2f2 0%,#d8d2c8 50%,#e8c54a 75%,#2f3d5c 100%)}
.photo--floor{background:linear-gradient(135deg,#efefef 0%,#b48a5e 60%,#7b5a3a 100%)}
.photo--grey{background:linear-gradient(135deg,#efefef 0%,#9a9a9a 60%,#5c5c5c 100%)}
.photo--illus{background:linear-gradient(180deg,#f4f4f4 0%,#c75b4b 45%,#8a9bb0 100%);border-radius:4px}
.photo--fence{background:linear-gradient(180deg,var(--green) 0%,#6aa83a 100%)}

/* headings */
.banner{position:absolute;background:var(--green);color:#fff;font-family:'Montserrat',sans-serif;font-weight:800;font-style:italic;letter-spacing:.3px}
.banner--about{left:40px;top:22px;width:175px;height:24px;font-size:12px;line-height:24px;padding-left:14px;clip-path:polygon(6% 0,100% 0,100% 100%,0 100%)}
.banner--why{left:0;top:128px;width:215.33px;height:34px;font-family:'Archivo Black',sans-serif;font-style:normal;font-weight:400;color:var(--ink);font-size:15px;line-height:34px;padding-left:16px}
.banner--services{left:0;top:118px;width:230px;height:34px;font-family:'Archivo Black',sans-serif;font-style:normal;font-weight:400;color:var(--ink);font-size:15px;line-height:34px;padding-left:12px;clip-path:polygon(0 0,100% 0,92% 100%,0 100%)}

.body-copy{font-size:5.6px;line-height:1.55;font-style:italic;color:var(--text)}
.body-copy p{margin-bottom:4px}

.subhead{font-weight:800;font-style:italic;font-size:9px;color:var(--ink);letter-spacing:.2px}

/* brand */
.brand{display:flex;align-items:center;justify-content:center;gap:7px;color:var(--ink);font-family:'Montserrat',sans-serif;font-weight:600;letter-spacing:2px}
.brand__dot{width:12px;height:12px;border-radius:50%;background:var(--green)}
.brand--cover{font-size:17px}
.brand--cover .brand__dot{width:16px;height:16px}
.brand--small{font-size:9px}
.brand--small .brand__dot{width:8px;height:8px}

.contact{text-align:center;color:var(--ink)}
.contact__title{color:var(--green);font-weight:700;font-size:10px;letter-spacing:.5px;margin:4px 0 6px}
.contact__line{font-size:8px;font-weight:600;display:flex;flex-direction:column;align-items:center;margin-bottom:4px}
.contact__line svg{margin-bottom:2px}

/* cover */
.cover-arc{position:absolute;left:-40px;top:330px;width:300px;height:300px;border-radius:50%;background:rgba(255,255,255,.93)}
.cover-title{position:absolute;left:14px;top:346px;width:190px;text-align:center;font-family:'Archivo Black',sans-serif;color:var(--green);font-size:21px;line-height:1}
.cover-title small{font-size:14px}
.cover-copy{position:absolute;left:16px;top:405px;width:186px;text-align:center;font-size:7.4px;line-height:1.5;color:var(--ink)}
.pill{position:absolute;background:var(--green);color:#fff;border-radius:14px;font-weight:700;text-align:center;letter-spacing:.3px}
.pill--cover{left:14px;top:458px;width:188px;height:24px;line-height:24px;font-size:8.5px}
.pill--why{left:16px;top:384px;width:184px;height:20px;line-height:20px;font-size:8px}

/* welcome */
.welcome{position:absolute;left:18px;top:24px;width:180px;text-align:center;font-size:6px;font-style:italic;line-height:1.5}
.rule{position:absolute;height:1.5px;background:var(--green)}

/* tiles */
.tiles{position:absolute;left:14px;top:180px;width:188px;display:grid;grid-template-columns:1fr 1fr;gap:6px}
.tile{height:90px;background:var(--tile);display:flex;flex-direction:column;align-items:center;justify-content:center;gap:8px}
.tile:nth-child(2),.tile:nth-child(3){background:var(--tile-dark)}
.tile__label{font-size:7.5px;font-weight:600;color:var(--ink);letter-spacing:.3px}

/* services */
.service{position:absolute;display:flex;gap:8px;width:196px}
.service__icon{flex:0 0 28px;height:28px;border-radius:50%;border:1.5px solid var(--green);display:flex;align-items:center;justify-content:center;margin-top:6px}
.service__title{font-size:6.6px;font-weight:800;color:var(--ink);line-height:1.25;margin-bottom:2px}
.service__text{font-size:5.6px;line-height:1.45;color:var(--text)}
</style>
</head>
<body>

<!-- Outside spread -->
<section class="spread spread--outside">
  <!-- About panel -->
  <article class="panel panel--about">
    <h2 class="banner banner--about">ABOUT OUR COMPANY</h2>
    <div class="abs body-copy" style="left:18px;top:58px;width:182px">
      <p>At Larkmore our goal is to ease your worries and help you with your journey in preparing your house for rental or resale.</p>
      <p>Whether it is a move to another residence or the difficult task of dealing with the grief when a loved one passes away, Larkmore can help with the preparation of the property for sale. Larkmore will come in, remove unwanted items and dispose of all rubbish, do cosmetic repairs if required and leave the property in a spotless state.</p>
      <p>Our trained and reliable staff repair any house and carry out landscaping in preparation for renting or resale of the property in a timely and professional manner. Our team provides a discreet and trustworthy service, keeping in mind the sensitive nature of the work.</p>
      <p>Larkmore will make sure that all remaining furniture and possessions left inside the property are removed, sold or taken to storage and the remainder of unwanted goods are sorted so that the entire property is completely cleared for rental or sale.</p>
    </div>
    <h3 class="abs subhead" style="left:18px;top:362px">DECEASED ESTATE CLEANUPS</h3>
    <div class="photo photo--fence" style="left:0;top:440px;width:215px;height:60px" role="img" aria-label="Green lawn band with white picket fence"></div>
    <div class="photo photo--illus" style="left:62px;top:384px;width:92px;height:74px" role="img" aria-label="Illustration of a house with a removal truck"></div>
  </article>

  <!-- Contact panel -->
  <article class="panel panel--contact">
    <p class="welcome">Welcome to Larkmore, a company that cares solely about your best interest and the care for the estate of your loved one.</p>
    <div class="rule" style="left:78px;top:66px;width:60px"></div>
    <div class="photo photo--warm" style="left:0;top:92px;width:216px;height:250px" role="img" aria-label="Photo of a brick home with a paved courtyard"></div>
    <div class="abs contact" style="left:0;top:362px;width:215px">
      <div class="brand brand--small"><span class="brand__dot"></span>LARKMORE</div>
      <p class="contact__title">CONTACT US</p>
      <p class="contact__line">
        <svg width="8" height="7" viewBox="0 0 8 7"><rect x=".5" y=".5" width="7" height="6" fill="none" stroke="var(--green)"/><path d="M.5 .5 4 4 7.5 .5" fill="none" stroke="var(--green)"/></svg>
        PO Box 248, Brookfield 3021</p>
      <p class="contact__line">
        <svg width="7" height="8" viewBox="0 0 7 8"><path d="M1 0h2l.6 2-1 .8a5 5 0 0 0 2 2.2l.9-.9L7 5v2L6 8C3 7.5.5 5 0 2z" fill="var(--green)"/></svg>
        0400 555 019</p>
      <p class="contact__line">
        <svg width="8" height="8" viewBox="0 0 8 8"><circle cx="4" cy="4" r="4" fill="var(--green)"/></svg>
        info@larkmore.com.au</p>
    </div>
  </article>

  <!-- Cover panel -->
  <article class="panel panel--cover">
    <div class="abs brand brand--cover" style="left:0;top:44px;width:215px"><span class="brand__dot"></span>LARKMORE</div>
    <div class="photo photo--couple" style="left:0;top:112px;width:216px;height:388px" role="img" aria-label="Photo of a smiling senior couple seated outside their brick home"></div>
    <div class="cover-arc"></div>
    <h1 class="cover-title">WE'RE<br>HERE <small>to</small> HELP</h1>
    <p class="cover-copy">At Larkmore our goal is to ease your worries and help you with your journey in preparing your house for rental or resale.</p>
    <p class="pill pill--cover">www.larkmore.com.au</p>
  </article>
</section>

<!-- Inside spread -->
<section class="spread spread--inside">
  <!-- Why choose us -->
  <article class="panel panel--why">
    <div class="photo photo--clean" style="left:0;top:0;width:216px;height:128px" role="img" aria-label="Photo of gloved hands cleaning a surface with spray bottle"></div>
    <h2 class="banner banner--why">WHY CHOOSE US</h2>
    <div class="tiles">
      <div class="tile">
        <svg width="36" height="40" viewBox="0 0 36 40"><polygon points="18,0 36,10 36,30 18,40 0,30 0,10" fill="var(--green)"/><path d="M11 20l5 5 9-10" fill="none" stroke="#fff" stroke-width="3"/></svg>
        <span class="tile__label">QUALITY</span>
      </div>
      <div class="tile">
        <svg width="36" height="40" viewBox="0 0 36 40"><polygon points="18,0 36,10 36,30 18,40 0,30 0,10" fill="var(--green)"/><polygon points="15,11 21,11 23,28 18,32 13,28" fill="#fff"/></svg>
        <span class="tile__label">PROFESSIONALISM</span>
      </div>
      <div class="tile">
        <svg width="36" height="40" viewBox="0 0 36 40"><polygon points="18,0 36,10 36,30 18,40 0,30 0,10" fill="var(--green)"/><circle cx="18" cy="20" r="8" fill="#fff"/></svg>
        <span class="tile__label">PRIDE</span>
      </div>
      <div class="tile">
        <svg width="36" height="40" viewBox="0 0 36 40"><polygon points="18,0 36,10 36,30 18,40 0,30 0,10" fill="var(--green)"/><circle cx="18" cy="20" r="8" fill="none" stroke="#fff" stroke-width="2.5"/></svg>
        <span class="tile__label">AREAS SERVICED</span>
      </div>
    </div>
    <p class="pill pill--why">www.larkmorevic.com.au</p>
    <div class="photo photo--grey" style="left:0;top:416px;width:216px;height:84px" role="img" aria-label="Black and white photo of mopping a floor"></div>
  </article>

  <!-- Services 1 -->
  <article class="panel panel--services">
    <div class="photo photo--floor" style="left:0;top:0;width:216px;height:118px" role="img" aria-label="Photo of a cleaner mopping a timber floor"></div>
    <h2 class="banner banner--services">SERVICES OFFERED</h2>
    <div class="service" style="left:10px;top:166px">
      <span class="service__icon"><svg width="14" height="14" viewBox="0 0 14 14"><circle cx="4.5" cy="3" r="2" fill="var(--green)"/><circle cx="9.5" cy="3" r="2" fill="var(--green)"/><rect x="2.5" y="6" width="4" height="8" fill="var(--green)"/><rect x="7.5" y="6" width="4" height="8" fill="var(--green)"/></svg></span>
      <div><p class="service__title">SENIOR / AGED CARE RELOCATIONS AND DOWN SIZING</p>
      <p class="service__text">If you're relocating into age care or downsizing your living arrangements, Larkmore offers you a complete service to assist you in moving to your new home.</p></div>
    </div>
    <div class="service" style="left:10px;top:248px">
      <span class="service__icon"><svg width="14" height="14" viewBox="0 0 14 14"><path d="M7 1 13 7h-2v6H3V7H1z" fill="var(--green)"/></svg></span>
      <div><p class="service__title">COSMETIC REPAIRS AND HOUSE MAINTENANCE</p>
      <p class="service__text">At Larkmore, we are experienced in Cosmetic Repairs, House Maintenance and house renovations and we can help you achieve the maximum.</p></div>
    </div>
    <div class="service" style="left:10px;top:322px">
      <span class="service__icon"><svg width="14" height="14" viewBox="0 0 14 14"><rect x="1" y="4" width="12" height="9" fill="none" stroke="var(--green)" stroke-width="1.5"/><path d="M0 4 7 0 14 4" fill="var(--green)"/></svg></span>
      <div><p class="service__title">DECEASED ESTATES</p>
      <p class="service__text">Losing a loved one and being left with the task of finalizing and clearing out a property can be difficult and traumatic for families to deal with. Let our professional team help with the daunting task of making decisions needed, easier for you.</p></div>
    </div>
    <div class="photo photo--grey" style="left:0;top:416px;width:216px;height:84px" role="img" aria-label="Black and white photo of a hand painting a window frame"></div>
  </article>

  <!-- Services 2 -->
  <article class="panel panel--services-more">
    <div class="photo photo--floor" style="left:0;top:0;width:216px;height:118px" role="img" aria-label="Photo of a bright hallway with polished floor"></div>
    <div class="service" style="left:10px;top:132px">
      <span class="service__icon"><svg width="14" height="14" viewBox="0 0 14 14"><rect x="4" y="5" width="7" height="9" rx="1" fill="var(--green)"/><rect x="5" y="1" width="4" height="4" fill="var(--green)"/><path d="M9 2h3" stroke="var(--green)" stroke-width="1.5"/></svg></span>
      <div><p class="service__title">CLEANING SERVICE</p>
      <p class="service__text">We can provide a Cleaning Service for a house sale or rental preparation or a deceased estate. Houses need to be cleared for the property market, but they also need to be cleaned thoroughly. Let us make these decisions easier for you.</p></div>
    </div>
    <div class="service" style="left:10px;top:220px">
      <span class="service__icon"><svg width="14" height="14" viewBox="0 0 14 14"><circle cx="5" cy="3" r="2" fill="var(--green)"/><rect x="3" y="6" width="4" height="8" fill="var(--green)"/><rect x="9" y="9" width="4" height="5" fill="var(--green)"/></svg></span>
      <div><p class="service__title">PREPARATION FOR RENTAL OR SALE</p>
      <p class="service__text">Our target is to create maximum appeal on all aspects of your property, allowing you to sell or rent.</p></div>
    </div>
    <div class="service" style="left:10px;top:284px">
      <span class="service__icon"><svg width="14" height="14" viewBox="0 0 14 14"><circle cx="7" cy="4" r="3" fill="var(--green)"/><path d="M7 7v3" stroke="var(--green)" stroke-width="1.5"/><rect x="3" y="10" width="8" height="4" fill="var(--green)"/></svg></span>
      <div><p class="service__title">GARDEN MAKEOVERS</p>
      <p class="service__text">We run a successful landscaping business, The Fernleaf Landscapes Division, offering a full service in landscaping and construction.</p></div>
    </div>
    <div class="photo photo--grey" style="left:0;top:360px;width:216px;height:140px" role="img" aria-label="Black and white photo of cleaning products and a bucket"></div>
  </article>
</section>

</body>
</html>
```